Packaging design for HOT NEW RETAIL BEARD OIL BRAND - Merrow Fennick Apothecary

Packaging design for beard oils. I've attached a brief, and I've also attached a few examples of bottles and boxes. Of course, we need an entirely unique look. I've attached the photo of Merrow Fennick as well - you can choose to use it or not (I'm open).

This product will be sold at national retailers and needs to look like a brand that is sold at boutique

What the consumer wants to see on the shelf:
-Box should larger than others and be soft touch (feels luxurious)
-More “hipster look/feel”
-Text should stand out like inspiration photos - jumping off the shelf to the consumer
-Use the existing logo of Merrow Fennick
-Deco will be wrap label as shown in current product image
-Sample text to pull copy for outer carton (taken from label on glass bottle):
-Strengthen and condition your beard with this blend of natural oils. Sunflower oil is rich in omega, fatty acids and vitamins E, C, B, and A, while avocado oil hydrates the beard fibers from root to tip, keep the beard looking and feeling extraordinary. Smooth into your beard for a healthy sheen and a woodsy scent evoking the great outdoors.
-Cool/Hipster product at discount pricing

Target Market(s)

Men from ages 20-40. Women also buy this product for their men, so it needs to look like a well known brand.

Industry/Entity Type

Hair And Beauty

Font styles to use
Sans Serif

Colors

Designer to choose colors to be used in the design.

Requirements
Must have
• A full label and box design with key call outs:
• Features and benefits - found in attached brief
• Description of what it is: Beard Oil
• Name of frangrance: Sandalwood
• Size: 2 oz / 60 ml
Nice to have
• Feel free to revamp the logo if needed. I am not married to the font for Merrow Fennick Apothecary.

```html
<!DOCTYPE html>
<html lang="en">
<head>
<meta charset="utf-8">
<title>Merrow Fennick Apothecary – Men's Beard Oil Packaging</title>
<link rel="stylesheet" href="https://fonts.googleapis.com/css2?family=Libre+Baskerville:wght@400;700&family=Courier+Prime:wght@400;700&family=Fredoka:wght@500;700&display=swap">
<style>
  :root {
    --bg: #a9ece4;
    --box-black: #1f1f1f;
    --label-navy: #2c2c44;
    --gold: #d9a443;
    --gold-light: #ecd49a;
    --white: #f2f2f2;
    --grey-type: #d8d8d8;
  }
  * { margin: 0; padding: 0; box-sizing: border-box; }
  html, body { width: 1200px; height: 1019px; overflow: hidden; }
  body { background: var(--bg); position: relative; font-family: "Courier Prime", monospace; }

  .box-front {
    position: absolute; left: 50px; top: 50px; width: 610px; height: 920px;
    background: var(--box-black); color: var(--white);
  }
  .brand { position: absolute; left: 0; right: 0; text-align: center; }
  .brand-name {
    font-family: "Libre Baskerville", serif; font-weight: 400; letter-spacing: -1px;
    text-transform: uppercase; line-height: 1;
  }
  .brand-sub {
    display: flex; align-items: center; justify-content: center;
    font-family: "Courier Prime", monospace; text-transform: uppercase; color: var(--grey-type);
  }
  .brand-sub::before, .brand-sub::after {
    content: ""; height: 3px; background: var(--gold); display: block;
  }
  .box-front .brand { top: 70px; }
  .box-front .brand-name { font-size: 46px; }
  .box-front .brand-sub { font-size: 24px; margin-top: 8px; gap: 14px; }
  .box-front .brand-sub::before, .box-front .brand-sub::after { width: 70px; }

  .art { position: absolute; }
  .mustache-art { left: 120px; top: 230px; width: 180px; height: 60px; background: var(--white); border-radius: 40px; }
  .head-art { left: 390px; top: 205px; width: 180px; height: 225px; background: linear-gradient(#f2f2f2, #dedede); border-radius: 80px 80px 60px 60px; }

  .tagline { position: absolute; left: 120px; top: 312px; font-size: 20px; color: var(--grey-type); letter-spacing: 1px; }
  .title {
    position: absolute; left: 60px; font-family: "Fredoka", sans-serif; font-weight: 700;
    color: var(--gold); text-transform: uppercase; line-height: 1; white-space: nowrap;
  }
  .box-front .title-mens { top: 345px; left: 120px; font-size: 84px; font-weight: 500; }
  .box-front .title-oil { top: 445px; font-size: 100px; letter-spacing: -2px; }
  .types { position: absolute; font-weight: 700; text-transform: uppercase; white-space: nowrap; }
  .box-front .types { left: 60px; top: 562px; font-size: 35px; letter-spacing: 1px; }

  .benefits { position: absolute; left: 60px; top: 630px; list-style: none; font-size: 26px; color: var(--grey-type); line-height: 1.45; text-transform: uppercase; }
  .benefits li::before { content: "• "; }
  .benefits li::after { content: " •"; }

  .scent {
    position: absolute; background: var(--gold); color: var(--white);
    font-family: "Fredoka", sans-serif; font-weight: 500; text-align: center;
  }
  .box-front .scent { left: 60px; top: 780px; width: 290px; height: 52px; line-height: 52px; font-size: 32px; }
  .size { position: absolute; font-weight: 700; }
  .box-front .size { left: 60px; top: 855px; font-size: 24px; }

  .bottle-label {
    position: absolute; left: 740px; top: 220px; width: 400px; height: 560px;
    background: var(--label-navy); color: var(--white);
  }
  .bottle-label .brand { top: 40px; }
  .bottle-label .brand-name { font-size: 28px; }
  .bottle-label .brand-sub { font-size: 14px; margin-top: 4px; gap: 8px; }
  .bottle-label .brand-sub::before, .bottle-label .brand-sub::after { width: 40px; height: 2px; }
  .label-head-art { left: 140px; top: 130px; width: 120px; height: 165px; background: linear-gradient(#f0f0f4, #dcdce4); border-radius: 50px 50px 40px 40px; }
  .bottle-label .title { left: 0; right: 0; text-align: center; }
  .bottle-label .title-mens { top: 315px; font-size: 44px; font-weight: 500; }
  .bottle-label .title-oil { top: 362px; font-size: 54px; }
  .bottle-label .types { left: 0; right: 0; top: 425px; text-align: center; font-size: 19px; }
  .label-band { position: absolute; left: 0; right: 0; top: 460px; bottom: 0; background: var(--gold-light); }
  .bottle-label .size { left: 0; right: 0; top: 470px; text-align: center; font-size: 14px; color: var(--label-navy); }
  .bottle-label .scent { left: 0; right: 0; top: 500px; height: 40px; line-height: 40px; font-size: 24px; background: var(--gold); }
</style>
</head>
<body>
  <section class="box-front">
    <div class="brand">
      <div class="brand-name">Merrow Fennick</div>
      <div class="brand-sub">Apothecary</div>
    </div>
    <div class="art mustache-art" role="img" aria-label="Illustration of a curled white moustache"></div>
    <div class="art head-art" role="img" aria-label="Illustration of a bearded man's head silhouette"></div>
    <div class="tagline">GENTLMEN ONLY</div>
    <div class="title title-mens">Men's</div>
    <div class="title title-oil">Beard Oil</div>
    <div class="types">For all beard types</div>
    <ul class="benefits">
      <li>Conditions dryness</li>
      <li>Softens roughness</li>
      <li>Combats discomfort</li>
    </ul>
    <div class="scent">Sandalwood</div>
    <div class="size">60ml / 2 fl.oz.</div>
  </section>

  <section class="bottle-label">
    <div class="brand">
      <div class="brand-name">Merrow Fennick</div>
      <div class="brand-sub">Apothecary</div>
    </div>
    <div class="art label-head-art" role="img" aria-label="Illustration of a bearded man's head silhouette"></div>
    <div class="title title-mens">Men's</div>
    <div class="title title-oil">Beard Oil</div>
    <div class="types">For all beard types</div>
    <div class="label-band"></div>
    <div class="size">60ml / 2 fl.oz.</div>
    <div class="scent">Sandalwood</div>
  </section>
</body>
</html>
```